Venture Capital Investment Firm

We are looking to overhaul our existing website (substantially), with only using the same logos (which we can provide).
We are an investment firm that focuses on making loans to late stage technology companies. Our site should ultimately look like other venture capital firms, and look modern and fresh. We have an existing website www.northvaleloan.com which this will be replacing, although we will be using a lot of the existing written content, and potentially the numbers of pages we will need, we are not wed to anything else. Please feel free to shoot any questions at any time and thank you in advance for your help!
Websites we like as examples:
https://www.tkbrandel.com/
https://www.emberwoodfunds.com/
Target Market(s)
Potential investors who will invest in our firm, as well as potentially companies that are looking to borrow money from us.

```html
<!DOCTYPE html>
<html lang="en">
<head>
<meta charset="utf-8">
<title>Northvale Loan – Strategy &amp; Team</title>
<link href="https://fonts.googleapis.com/css2?family=Lato:wght@300;400;700&display=swap" rel="stylesheet">
<style>
:root{
  --bg:#e3f0fa;
  --navy:#03215a;
  --link:#2b8fd6;
  --ink:#1f2a44;
  --body:#5c6478;
  --muted:#8a90a0;
  --rule:#e6e8ee;
  --sky-a:#7cc3f0;
  --sky-b:#4ea3e2;
  --peri-a:#a9b6f6;
  --peri-b:#7d92ee;
  --photo-a:#d9d9d9;
  --photo-b:#4a4a4a;
}
*{box-sizing:border-box;margin:0;padding:0}
html,body{width:1200px;height:1042px;overflow:hidden}
body{background:var(--bg);font-family:'Lato',sans-serif;position:relative}
.page{position:absolute;background:#fff;overflow:hidden;box-shadow:0 6px 24px rgba(3,33,90,.08)}
.site-header{position:absolute;left:0;top:0;right:0;background:var(--navy);display:flex;align-items:center}
.brand{display:flex;align-items:center;gap:6px;color:#fff;font-weight:400;letter-spacing:.06em;position:absolute}
.brand-dot{border:1.5px solid #fff;border-radius:50%}
.nav{position:absolute;display:flex;text-transform:uppercase;color:var(--link);font-weight:400}
.nav .current{color:#fff}

/* team page */
.team{left:83px;top:0;width:487px;height:852px}
.team .site-header{height:40px}
.team .brand{left:40px;top:12px;font-size:10px}
.team .brand-dot{width:13px;height:13px}
.team .nav{left:203px;top:15px;gap:9.6px;font-size:6px}
.team h1{position:absolute;left:40px;top:63px;font-weight:300;font-size:18px;color:var(--link)}
.member{position:absolute;left:0;width:487px;height:236px}
.member .photo{position:absolute;left:57px;top:0;width:98px;height:95px;background:linear-gradient(180deg,var(--photo-a) 0%,#fff 30%,var(--photo-b) 100%)}
.member .links{position:absolute;left:57px;top:105px;font-size:5.5px;color:var(--link);line-height:13px}
.member .links span{display:flex;align-items:center;gap:5px;text-decoration:underline}
.member .links i{display:inline-block;width:8px;height:8px;background:var(--link);border-radius:1px}
.member .name{position:absolute;left:179px;top:-4px;font-size:12px;color:var(--ink)}
.member .role{position:absolute;left:179px;top:14px;font-size:7px;color:var(--ink);font-weight:300;letter-spacing:.02em}
.member .focus{position:absolute;left:179px;top:30px;font-size:5.5px;color:var(--ink)}
.member .bio{position:absolute;left:179px;top:46px;width:300px;font-size:5.6px;line-height:9.8px;color:var(--muted);font-weight:300}
.member .bio p{margin-bottom:9.8px}
.team .rule{position:absolute;left:42px;width:440px;height:1px;background:var(--rule)}
.team footer{position:absolute;left:57px;top:802px;font-size:5.6px;line-height:8px;color:var(--muted);font-weight:300}
.team footer a{color:var(--link);text-decoration:underline}

/* strategy page */
.strategy{left:400px;top:131px;width:714px;height:911px}
.strategy .site-header{height:60px}
.strategy .brand{left:60px;top:21px;font-size:16px}
.strategy .brand-dot{width:20px;height:20px}
.strategy .nav{left:300px;top:24px;gap:14px;font-size:9.6px}
.strategy h1{position:absolute;left:59px;top:92px;font-weight:300;font-size:27px;color:var(--link)}
.strategy h2{position:absolute;left:60px;font-weight:400;font-size:18px;color:var(--ink)}
.strategy h3{position:absolute;left:60px;font-weight:300;font-size:12px;color:var(--ink);letter-spacing:.02em}
.strategy p.copy{position:absolute;left:59px;font-size:9px;line-height:14.3px;color:var(--body);font-weight:300}
.strategy .rule{position:absolute;left:60px;width:573px;height:1px;background:var(--rule)}
.circle{position:absolute;width:88px;height:88px;margin:-44px 0 0 -44px;border-radius:50%;display:flex;align-items:flex-end;justify-content:center;padding-bottom:22px;text-align:center;font-weight:700;font-size:9px;line-height:11px;color:var(--navy)}
.circle.sky{background:radial-gradient(circle at 50% 40%,var(--sky-a),var(--sky-b))}
.circle.peri{background:radial-gradient(circle at 50% 40%,var(--peri-a),var(--peri-b))}
</style>
</head>
<body>

<section class="page team">
  <header class="site-header">
    <div class="brand"><span class="brand-dot"></span>NORTHVALE LOAN</div>
    <nav class="nav"><span>Home</span><span>Strategy</span><span>About us</span><span class="current">Team</span><span>News</span><span>Contact</span><span>Investors</span></nav>
  </header>
  <h1>Senior Team</h1>

  <article class="member" style="top:98px">
    <div class="photo" role="img" aria-label="Portrait of Elias Brandt"></div>
    <div class="links"><span><i></i>Profile</span><span><i></i>Email</span></div>
    <div class="name">Elias Brandt</div>
    <div class="role">MANAGING PARTNER</div>
    <div class="focus">Life Sciences, Technology</div>
    <div class="bio">
      <p>Elias Brandt is an industry leader with over $1.2 billion invested since 2004. Elias focuses on origination, underwriting and portfolio work at Northvale Loan.</p>
      <p>Mr. Brandt was the co-founder of a healthcare structured credit fund from 2010-2014. Before that he was a Director and Co-Head of the Healthcare Group at Harbor Ridge Group.</p>
      <p>Prior to joining Harbor Ridge, Mr. Brandt executed mezzanine debt and leveraged loans for growth companies. Previously, he worked in leveraged finance, where he structured and underwrote bank loan and high yield deals. He holds joint law and business degrees.</p>
    </div>
  </article>
  <div class="rule" style="top:316px"></div>

  <article class="member" style="top:334px">
    <div class="photo" role="img" aria-label="Portrait of Samir Okafor"></div>
    <div class="links"><span><i></i>Profile</span><span><i></i>Email</span></div>
    <div class="name">Samir Okafor</div>
    <div class="role">MANAGING PARTNER</div>
    <div class="focus">Technology</div>
    <div class="bio">
      <p>Samir Okafor leads technology investment origination and brings over 15 years of technology investment and transaction experience.</p>
      <p>Mr. Okafor was a Managing Director and Head of a mergers practice in Bay City from 2011. Earlier he was a Managing Director at a global bank in Bay City, focused on semiconductors and hardware, and spent over 7 years as co-head of a semiconductor banking practice.</p>
      <p>As an investment banker, Samir worked globally with companies, venture capitalists and technology partners on deals totaling in excess of $75B. He holds an MBA and an MSc in finance.</p>
    </div>
  </article>
  <div class="rule" style="top:552px"></div>

  <article class="member" style="top:570px">
    <div class="photo" role="img" aria-label="Portrait of Daniel Marsh"></div>
    <div class="links"><span><i></i>Profile</span><span><i></i>Email</span></div>
    <div class="name">Daniel Marsh</div>
    <div class="role">PARTNER</div>
    <div class="focus">Chief Operating Officer</div>
    <div class="bio">
      <p>Daniel Marsh serves as the Chief Operating Officer and has long experience in the alternative-investment markets, including private credit, operations, capital-raising, investor relations and portfolio work.</p>
      <p>Before joining Northvale Loan, Mr. Marsh served as a Managing Partner at a venture firm in Bay City and as a Managing Director at a placement firm, where he raised over $15 billion. He also worked as a finance attorney advising technology companies and investors.</p>
      <p>Mr. Marsh received a BA and a law degree with honors.</p>
    </div>
  </article>
  <div class="rule" style="top:775px"></div>

  <footer>
    NORTHVALE LOAN, BAY CITY<br>
    © 2015 Northvale Loan Partners LLC. All Rights Reserved.<br>
    <a>Legal Disclaimer</a>
  </footer>
</section>

<section class="page strategy">
  <header class="site-header">
    <div class="brand"><span class="brand-dot"></span>NORTHVALE LOAN</div>
    <nav class="nav"><span>Home</span><span class="current">Strategy</span><span>About us</span><span>Team</span><span>News</span><span>Contact</span><span>Investors</span></nav>
  </header>

  <h1>Our Strategy</h1>
  <h2 style="top:139px">Partners for growth</h2>
  <p class="copy" style="top:168px">We provide flexible capital to innovative companies and their investors</p>
  <div class="rule" style="top:203px"></div>

  <h3 style="top:226px">INDUSTRY FOCUS</h3>
  <p class="copy" style="top:252px;width:560px">Our focus spans the life science and technology industries, two sectors where intellectual property (IP) is an integral driver of asset and enterprise value.</p>
  <p class="copy" style="top:294px;width:580px">Our broad experience in investing, technology evaluation, and product forecasting affords us a unique understanding of the value of assets in these dynamic sectors, allowing us to see value where others cannot.</p>
  <div class="rule" style="top:340px"></div>

  <h3 style="top:357px">LIFE SCIENCES</h3>
  <p class="copy" style="top:382px;width:240px">We have a long track record of partnering with companies and investors that create and commercialize life science products, with extensive experience spanning biopharmaceuticals, medical devices, and tools &amp; diagnostics.</p>
  <div class="circle sky" style="left:408px;top:405px">Biopharma</div>
  <div class="circle sky" style="left:488px;top:405px">Devices</div>
  <div class="circle sky" style="left:568px;top:405px">Tools &amp;<br>Diagnostics</div>
  <div class="rule" style="top:474px"></div>

  <h3 style="top:499px">TECHNOLOGY</h3>
  <p class="copy" style="top:523px;width:236px">We uniquely offer sizeable and flexible structured credit financing solutions to innovative technology companies, with a focus on enterprise software, data &amp; analytics, semiconductors, and communications systems.</p>
  <div class="circle peri" style="left:408px;top:541px">Software &amp;<br>Services</div>
  <div class="circle peri" style="left:488px;top:541px">Hardware</div>
  <div class="circle peri" style="left:568px;top:541px">Systems</div>
  <div class="rule" style="top:618px"></div>

  <h3 style="top:642px">TRANSACTION TYPES</h3>
  <p class="copy" style="top:668px;width:246px">Northvale Loan's proven strategy focuses on identifying opportunities where demonstrated commercial success has established underlying asset or enterprise value prior to our investment. We tailor our financing solutions to each situation with the goal of preserving our partners' ownership interests, aligning incentives, and providing operating flexibility to build businesses of value.<br>Our approach enables us to work flexibly to meet the needs of companies, investors, and entrepreneurs we partner with through a wide array of transaction structures:</p>
  <div class="circle sky" style="left:408px;top:689px">Structured<br>Credit</div>
  <div class="circle sky" style="left:488px;top:689px">Milestones<br>&amp; Royalties</div>
  <div class="circle sky" style="left:568px;top:689px">Legacy<br>Assets</div>
  <div class="rule" style="top:829px"></div>

  <h2 style="top:849px">Key benefits</h2>
  <p class="copy" style="top:880px;width:600px">We seek to fill a void in the capital markets where too often complexity and perceived risk penalize innovative companies with proven products. We apply our team's deep domain knowledge to identify situations where our structured financing alternatives can deliver a lower cost of capital</p>
</section>

</body>
</html>
```